Flyer-Design für Rasseclub
sehr angenehme Zusammenarbeit - tolle Vorschläge - Anregungen werden prompt umgesetzt. Vielen Dank für den schönen Flyer. Vom Drucker habe ich auch noch ein Lob erhalten. "Nicht jeder Grafiker / Designer liefere solche gute Qualität ab"
Zielgruppe
Wir sind ein Rasseclub für die Zebu-Züchter in der Schweiz. Wir setzen uns für die Interessen und die Verbreitung der Zeburinder ein. Mit unserem Flyer versuchen wir interessierten Personen einen kurzen Überblick über die Rasse zu verschaffen.
Aufgabenstellung
Wir wünschen uns einen Flyer im A4 Format, welcher 1 oder 2x gefalzt ist. Vorne und hinten Beschriftet / Gestaltet.

```html
<!DOCTYPE html>
<html lang="de">
<head>
<meta charset="utf-8">
<title>Rasseclub Zebu Alpenland – Flyer</title>
<link rel="stylesheet" href="https://fonts.googleapis.com/css2?family=Open+Sans:wght@300;400;600;700&display=swap">
<style>
:root{
  --board:#e4e4e4;
  --olive:#5d6a37;
  --olive-light:#7b8752;
  --orange:#e2501b;
  --white:#ffffff;
  --ink:#2a2a2a;
  --photo-green:#6f8a3f;
  --photo-brown:#5a4236;
}
*{box-sizing:border-box;margin:0;padding:0}
html,body{width:1200px;height:3904px;overflow:hidden}
body{background:var(--board);font-family:"Open Sans",Arial,sans-serif;color:var(--ink);position:relative}
.sheet{position:absolute;display:flex;height:677px;box-shadow:0 4px 8px rgba(0,0,0,.28)}
.panel{position:relative;width:320px;height:677px;overflow:hidden;display:flex;flex-direction:column}
.bar-orange{height:16px;background:var(--orange);flex:none}
.band{height:18px;background:var(--olive-light);flex:none}
.photo{flex:none}
.photo-cow{background:linear-gradient(180deg,#a9b98a 0%,#8aa35a 45%,var(--photo-green) 75%,#b8a487 100%);position:relative}
.photo-cow::after{content:"";position:absolute;left:32%;top:18%;width:40%;height:62%;border-radius:40%;background:radial-gradient(ellipse at 50% 45%,var(--photo-brown),rgba(90,66,54,0) 70%)}
.photo-head{background:linear-gradient(135deg,#cfd3cc 0%,#9aa08c 35%,#6b5b4d 60%,#5b4c40 100%)}
.logo-head{height:118px;background:var(--white);display:flex;align-items:center;justify-content:center;gap:10px;flex:none}
.logo-dot{width:14px;height:14px;border-radius:50%;background:var(--orange)}
.logo-name{font-weight:700;font-size:22px;letter-spacing:1px;color:var(--ink)}
.cover-title{flex:1;background:var(--olive);color:var(--white);text-align:right;padding:38px 58px 0 0}
.cover-title .kicker{font-weight:300;font-size:20px;line-height:1.2}
.cover-title .name{font-weight:700;font-size:25px;letter-spacing:.5px;line-height:1.4}
h2{font-weight:700;font-size:13.5px;letter-spacing:.2px;text-transform:uppercase;white-space:nowrap;padding-bottom:10px;margin-bottom:16px;border-bottom:2px solid var(--orange);width:100%}
p{font-size:10.5px;line-height:1.3;margin-bottom:8px}
.text-white{flex:1;background:var(--white);padding:26px 30px 0 32px}
.club{flex:1;background:var(--olive);color:var(--white);padding:56px 36px 0 32px;position:relative}
.contact{position:absolute;left:32px;top:294px;font-size:10.5px;line-height:1.5}
.contact strong{font-weight:600}
.holder-box{position:absolute;left:32px;top:468px;width:251px;height:155px;background:var(--white);padding:16px 12px;font-size:10.5px;color:var(--olive)}
.inside{width:960px;background:linear-gradient(180deg,#ffffff 0%,#ffffff 30%,#e9ebe6 40%,#bfc6b2 48%,#7f9a4c 62%,var(--photo-green) 100%)}
.inside .cols{flex:1;display:flex}
.inside .col{width:320px;padding:48px 30px 0 40px}
.inside .col+.col{border-left:1px solid rgba(0,0,0,.25)}
.pasture{flex:1;background:linear-gradient(180deg,#ffffff 0%,#ffffff 36%,#e6e8e2 44%,#a6b28e 54%,#7f9a4c 66%,var(--photo-green) 100%)}
.pasture .col{padding:48px 30px 0 40px}
</style>
</head>
<body>

<div class="sheet" style="left:438px;top:88px">
  <section class="panel">
    <div class="logo-head"><span class="logo-dot"></span><span class="logo-name">ALPZEBU</span></div>
    <div class="photo photo-cow" style="height:392px" role="img" aria-label="Foto: dunkelbrauner Zebu-Stier auf einer Wiese"></div>
    <div class="band"></div>
    <div class="cover-title"><div class="kicker">Rasseclub</div><div class="name">ZEBU ALPENLAND</div></div>
    <div class="bar-orange"></div>
  </section>
</div>

<div class="sheet" style="left:120px;top:845px">
  <section class="panel">
    <div class="photo photo-head" style="height:367px" role="img" aria-label="Foto: Kopf eines Zebu-Rindes am Gatter"></div>
    <div class="band"></div>
    <div class="text-white">
      <h2>Herkunft</h2>
      <p>Die Zebus (Bos indicus) gehören zu den Buckelrindern, die sich nicht nur vom Erbgut, sondern auch vom äusseren Erscheinungsbild her stark von den anderen Rinderrassen in Europa unterscheiden. Die Zebus stammen ursprünglich aus Sri Lanka und dem südlichen Kaukasus. Heute sind sie auf der ganzen Welt verbreitet. Die Zeburasse wird in 600 Rasseschläge unterteilt: vom kleinsten Zwergzebu bis zu den grössten Brahma oder Nelore. Das Wort Zebu wird vom tibetanischen Wort „zeu“ respektive „zeba“ abgeleitet, welches übersetzt Buckel heisst.</p>
    </div>
    <div class="bar-orange"></div>
  </section>
  <section class="panel">
    <div class="club">
      <h2>Rasseclub</h2>
      <p>Bei «Herdenverband Alpenweide» sind über 150 Muttertiere der Rasse Zwergzebu und Zebu registriert. Der «Rasseclub Zebu Alpenland» gibt es seit dem Jahr 2015. Alle, die Zebus in der Schweiz halten, sind im Rasseclub herzlich willkommen. Die Tiere können, wie jedes andere Rind auch, bei «Herdenverband Alpenweide» angemeldet werden. Selbstverständlich können auch die anerkannten Stiere im Herdebuch aufgenommen werden und sind somit als Zuchtstiere anerkannt.</p>
      <div class="contact"><strong>Rasseclub Zebu Alpenland</strong><br>Talackerweg 12<br>8765 Feldbach<br>Tel. 031 555 20 40</div>
      <div class="holder-box">Ihr Zebuhalter in der Nähe:</div>
    </div>
    <div class="bar-orange"></div>
  </section>
  <section class="panel">
    <div class="logo-head"><span class="logo-dot"></span><span class="logo-name">ALPZEBU</span></div>
    <div class="photo photo-cow" style="height:392px" role="img" aria-label="Foto: dunkelbrauner Zebu-Stier auf einer Wiese"></div>
    <div class="band"></div>
    <div class="cover-title"><div class="kicker">Rasseclub</div><div class="name">ZEBU ALPENLAND</div></div>
    <div class="bar-orange"></div>
  </section>
</div>

<div class="sheet" style="left:120px;top:1588px">
  <section class="panel inside" role="img" aria-label="Foto: Herde Zebus frisst Heu am Zaun auf nebliger Weide">
    <div class="cols">
      <div class="col">
        <h2>Merkmale und Eigenschaften</h2>
        <p>Der Buckel ist das auffälligste, äussere Merkmal der Zeburinder. Das ausgesprochen marmorierte Buckelfleisch ist eine Delikatesse. Das übrige Muskelfleisch ist sehr fettarm, mit einem leichten Wildgeschmack, feinfaserig und enthält die gesunden Omega-3-Fettsäuren.</p>
        <p>Zum typischen Erscheinungsbild der Zebus gehören neben dem Buckel die Hörner, eine starke Wamme, ein abgezogenes und stark abgedachtes Becken, feine Extremitäten und eine schmale Stirn, die dem Kopf eine längliche Form verleiht.</p>
      </div>
      <div class="col">
        <p>Die Grösse der Tiere kann stark variieren. Die Kühe sind deutlich kleiner als die Stiere. Zebus kommen in allen Farben und Farbkombinationen vor. Auch die Hörner sind nicht immer klassisch nach oben gerichtet.</p>
        <p>Zebus sind sehr robust und gehören zu den extensiven Rinderrassen. Die Klauenpflege kann auf ein Minimum beschränkt werden. Die Tiere sind betreffend Futter sehr genügsam. Ihnen reicht im Sommer Gras und im Winter Heu. Auf Kraftfutter und andere Zusätze, mit Ausnahme von Salz, kann verzichtet werden. Die Abkalbung ist meist leicht und geschieht ohne menschliche Hilfe. Die Mutterkühe haben einen guten Schutzinstinkt für ihre Kälber.</p>
      </div>
      <div class="col">
        <p>Während die meisten europäischen Rinderrassen unter der Sommerhitze leiden, fühlen sich Zebus bei Temperaturen um 30 Grad noch wohl. Ihr schütteres Fell und die dicke Aussenhaut schützen sie vor der Hitze. In den letzten Jahren wurde beobachtet, dass Zebusperma auch bei Temperaturen über 38°C noch befruchtungsfähig bleibt. Kalte Temperaturen sind sie sich von ihrer Heimat auch gewohnt.</p>
        <h2 style="margin-top:22px">Einsatz</h2>
        <p>Durch ihr leichtes Gewicht verursachen Zebus kaum Trittschäden, wodurch sie fast überall einsetzbar sind. Sie können auch gut zur allgemeinen Landschaftspflege eingesetzt werden.</p>
      </div>
    </div>
    <div class="bar-orange"></div>
  </section>
</div>

<div class="sheet" style="left:276px;top:2379px">
  <section class="panel">
    <div class="pasture" role="img" aria-label="Foto: Zebus fressen Heu auf nebliger Weide">
      <div class="col">
        <h2>Merkmale und Eigenschaften</h2>
        <p>Der Buckel ist das auffälligste, äussere Merkmal der Zeburinder. Das ausgesprochen marmorierte Buckelfleisch ist eine Delikatesse. Das übrige Muskelfleisch ist sehr fettarm, mit einem leichten Wildgeschmack, feinfaserig und enthält die gesunden Omega-3-Fettsäuren.</p>
        <p>Zum typischen Erscheinungsbild der Zebus gehören neben dem Buckel die Hörner, eine starke Wamme, ein abgezogenes und stark abgedachtes Becken, feine Extremitäten und eine schmale Stirn, die dem Kopf eine längliche Form verleiht.</p>
      </div>
    </div>
    <div class="bar-orange"></div>
  </section>
  <section class="panel">
    <div class="photo photo-head" style="height:367px" role="img" aria-label="Foto: Kopf eines Zebu-Rindes am Gatter"></div>
    <div class="band"></div>
    <div class="text-white">
      <h2>Herkunft</h2>
      <p>Die Zebus (Bos indicus) gehören zu den Buckelrindern, die sich nicht nur vom Erbgut, sondern auch vom äusseren Erscheinungsbild her stark von den anderen Rinderrassen in Europa unterscheiden. Die Zebus stammen ursprünglich aus Sri Lanka und dem südlichen Kaukasus. Heute sind sie auf der ganzen Welt verbreitet. Die Zeburasse wird in 600 Rasseschläge unterteilt: vom kleinsten Zwergzebu bis zu den grössten Brahma oder Nelore. Das Wort Zebu wird vom tibetanischen Wort „zeu“ respektive „zeba“ abgeleitet, welches übersetzt Buckel heisst.</p>
    </div>
    <div class="bar-orange"></div>
  </section>
</div>

<div class="sheet" style="left:438px;top:3113px">
  <section class="panel">
    <div class="club">
      <h2>Rasseclub</h2>
      <p>Bei «Herdenverband Alpenweide» sind über 150 Muttertiere der Rasse Zwergzebu und Zebu registriert. Der «Rasseclub Zebu Alpenland» gibt es seit dem Jahr 2015. Alle, die Zebus in der Schweiz halten, sind im Rasseclub herzlich willkommen. Die Tiere können, wie jedes andere Rind auch, bei «Herdenverband Alpenweide» angemeldet werden. Selbstverständlich können auch die anerkannten Stiere im Herdebuch aufgenommen werden und sind somit als Zuchtstiere anerkannt.</p>
      <div class="contact"><strong>Rasseclub Zebu Alpenland</strong><br>Talackerweg 12<br>8765 Feldbach<br>Tel. 031 555 20 40</div>
      <div class="holder-box">Ihr Zebuhalter in der Nähe:</div>
    </div>
    <div class="bar-orange"></div>
  </section>
</div>

</body>
</html>
```